Visitenkarten-Design für Stillberaterin
Zielgruppe
Ich bin Stillberaterin ZMRPT, d. h. ich berate Mütter bei Stillschwierigkeiten. Meine Zielgruppe sind junge Familien, die sich vorab über das Stillen Ihres Kindes informieren möchten, Stillschwierigkeiten (z. B. Schmerzen, schlechte Gewichtszunahme usw.) haben oder Fragen rund ums Stillen haben (Medikamente, Stillen in besonderen Situationen...). Weiterhin biete ich Kurse für den Beikoststart oder zum Abstillen an.
Aufgabenstellung
Auf meiner Visitenkarte sollte mein Logo sowie alle Kontaktdaten klar und deutlich erkennbar sein. Die Farben sind dem Logo anzupassen. Die Schriftarten, die im Logo verwendet werden sind: Be Bright und Apple Tree

```html
<!DOCTYPE html>
<html lang="de">
<head>
<meta charset="utf-8">
<title>Sanft-und-Nah – Visitenkarte</title>
<link href="https://fonts.googleapis.com/css2?family=Great+Vibes&family=Andika&family=Carlito&family=Didact+Gothic&display=swap" rel="stylesheet">
<style>
  :root {
    --stage: #333333;
    --paper: #ffffff;
    --brand-pink: #ef5ba1;
    --soft-pink: #f7bfd9;
    --ink: #2b2b2b;
    --script-grey: #6d6d6d;
    --rule: #555555;
  }
  * { margin: 0; padding: 0; box-sizing: border-box; }
  html, body { width: 1073px; height: 1200px; overflow: hidden; }
  body { background: var(--stage); position: relative; }

  .card { position: absolute; left: 175px; width: 723px; height: 460px; box-shadow: 0 2px 6px rgba(0,0,0,.35); }
  .card--front { top: 101px; background: var(--paper); }
  .card--back { top: 623px; background: var(--brand-pink); }

  /* front */
  .brand-mark { position: absolute; left: 40px; top: 206px; width: 210px; display: flex; justify-content: center; align-items: center; gap: 8px; }
  .brand-mark__dot { width: 12px; height: 12px; border-radius: 50%; background: var(--brand-pink); flex: none; }
  .brand-mark__name { font-family: "Great Vibes", cursive; font-size: 28px; line-height: 1.2; color: var(--brand-pink); white-space: nowrap; }

  .divider { position: absolute; left: 271px; top: 84px; width: 1px; height: 303px; background: var(--rule); }

  .person { position: absolute; left: 337px; top: 80px; }
  .person__name { font-family: "Great Vibes", cursive; font-size: 50px; font-weight: 400; color: var(--script-grey); line-height: 1; }
  .person__role { margin-top: 22px; font-family: "Andika", sans-serif; font-size: 17px; line-height: 27px; color: var(--ink); }
  .address { margin-top: 26px; font-family: "Carlito", sans-serif; font-size: 22px; line-height: 31px; color: var(--ink); }
  .contact { margin-top: 18px; list-style: none; font-family: "Carlito", sans-serif; font-size: 22px; line-height: 31px; color: var(--ink); }
  .contact li { display: flex; align-items: center; }
  .contact svg { width: 20px; height: 20px; margin-right: 12px; fill: var(--brand-pink); flex: none; }

  /* back */
  .back-mark { position: absolute; left: 316px; top: 110px; width: 90px; height: 90px; border-radius: 50%; border: 3px solid var(--soft-pink); }
  .back-name { position: absolute; left: 0; right: 0; top: 242px; text-align: center; font-family: "Great Vibes", cursive; font-size: 68px; line-height: 1; color: var(--soft-pink); }
  .back-tagline { position: absolute; left: 0; right: 0; top: 320px; text-align: center; font-family: "Didact Gothic", sans-serif; font-size: 19px; color: var(--soft-pink); }
  .web-row { position: absolute; left: 0; right: 0; top: 404px; display: flex; justify-content: center; align-items: center; gap: 16px; }
  .web-row__url { font-family: "Great Vibes", cursive; font-size: 32px; color: var(--paper); }
  .flourish { width: 80px; height: 14px; border-radius: 7px; background: linear-gradient(90deg, rgba(255,255,255,0), rgba(255,255,255,.45), rgba(255,255,255,0)); }
</style>
</head>
<body>
  <section class="card card--front">
    <div class="brand-mark">
      <span class="brand-mark__dot"></span>
      <span class="brand-mark__name">Sanft-und-Nah</span>
    </div>
    <div class="divider"></div>
    <div class="person">
      <h1 class="person__name">Rubinka Tovik</h1>
      <p class="person__role">Fachkinderkrankenschwester,<br>Still- &amp; Laktationsberaterin ZMRPT</p>
      <p class="address">Am Lindenhang 12<br>93155 Hemau</p>
      <ul class="contact">
        <li>
          <svg viewBox="0 0 24 24" aria-hidden="true"><path d="M6.6 10.8a15 15 0 0 0 6.6 6.6l2.2-2.2c.3-.3.7-.4 1-.2 1.1.4 2.3.6 3.6.6.6 0 1 .4 1 1V20c0 .6-.4 1-1 1A17 17 0 0 1 3 4c0-.6.4-1 1-1h3.5c.6 0 1 .4 1 1 0 1.3.2 2.5.6 3.6.1.3 0 .7-.2 1z"/></svg>
          09402 4471820
        </li>
        <li>
          <svg viewBox="0 0 24 24" aria-hidden="true"><path d="M2 5h20v14H2z" fill="var(--brand-pink)"/><path d="M3 6l9 7 9-7M3 18l7-6M21 18l-7-6" stroke="#fff" stroke-width="1.2" fill="none"/></svg>
          rubinka@sanft-und-nah.de
        </li>
      </ul>
    </div>
  </section>

  <section class="card card--back">
    <div class="back-mark"></div>
    <p class="back-name">Sanft-und-Nah</p>
    <p class="back-tagline">Stillberatung für Regensburg</p>
    <div class="web-row">
      <div class="flourish" role="img" aria-label="Verzierung"></div>
      <span class="web-row__url">www.sanft-und-nah.de</span>
      <div class="flourish" role="img" aria-label="Verzierung"></div>
    </div>
  </section>
</body>
</html>
```